Tarnbrook Secondary College House displays

Our school has 4 new houses that are designed to promote school connectedness and school pride. Each house display should include the name of the house, a silhouette portrait of the person the house is named after and a famous quote from that person. Each house display should also promote the unique house colour. Details are included in the attached word document. I have also attached a Mark Dwyfor poster that gives some sort of idea about the look and feel we are after. The house name should be quite prominent.

Target Market(s)

Tarnbrook Secondary College has 1800 students. We are a unique school committed to a strengths based program. Our house system is designed to connect students to each other and to the school. To understand our school visit our website at www.tarnbrooksc.example.edu.au

Logo Text

We want a logo for each of our houses that has the house name on it - see the attached word document for details.

Font styles to use
Sans Serif

Colors
0792cd
00a990
fbed22
ec1f27

Requirements
Must have
• Colour- each house must include the colour it is aligned to. This is outlined in the attached word document

```html
<!DOCTYPE html>
<html lang="en">
<head>
<meta charset="utf-8">
<title>Tarnbrook Secondary College – House Displays</title>
<link rel="stylesheet" href="https://fonts.googleapis.com/css2?family=Raleway:wght@500;600;800&family=Caveat+Brush&display=swap">
<style>
  :root {
    --yellow: #e3e42d;
    --blue: #08aeef;
    --teal: #00c4ab;
    --red: #e00000;
    --ink: #111111;
    --navy: #10115a;
    --paper: #ffffff;
  }
  * { box-sizing: border-box; margin: 0; padding: 0; }
  html, body { width: 1200px; height: 1200px; overflow: hidden; background: var(--paper); }
  body { font-family: "Raleway", sans-serif; position: relative; }

  .house-panel { position: absolute; width: 596px; height: 596px; overflow: hidden; }
  .house-panel--marok { left: 0; top: 0; background: var(--yellow); color: var(--ink); }
  .house-panel--strand { left: 604px; top: 0; background: var(--blue); color: var(--navy); }
  .house-panel--vale { left: 0; top: 604px; background: var(--teal); color: var(--navy); }
  .house-panel--ashby { left: 604px; top: 604px; background: var(--red); color: var(--paper); }

  .house-tab { position: absolute; top: 0; width: 140px; height: 136px; }
  .house-tab svg { position: absolute; inset: 0; width: 100%; height: 100%; }
  .house-tab__label { position: relative; line-height: 0.98; text-align: center; }
  .house-tab__name { display: block; font-weight: 800; font-size: 31px; letter-spacing: 0.2px; }
  .house-tab__word { display: block; font-weight: 500; font-size: 32px; }
  .house-panel--marok .house-tab__label { color: var(--ink); }
  .house-panel--strand .house-tab__label,
  .house-panel--vale .house-tab__label { color: var(--navy); }
  .house-panel--ashby .house-tab__label { color: var(--red); }

  .college-name { position: absolute; right: 30px; width: 230px; text-align: center; font-size: 17px; line-height: 1.3; }
  .college-name strong { display: block; font-weight: 800; }
  .college-name span { font-weight: 500; }

  .namesake-photo { position: absolute; inset: 0; }

  .namesake-name { position: absolute; font-family: "Caveat Brush", cursive; font-weight: 400; line-height: 1; white-space: nowrap; }
  .namesake-quote { position: absolute; font-weight: 500; }

  .caption-box { position: absolute; left: 0; background: var(--paper); padding: 12px 14px 0 26px; font-size: 9.5px; line-height: 1.3; font-weight: 500; }
  .house-panel--marok .caption-box { padding: 10px 8px 0 6px; color: var(--ink); font-size: 8.5px; }
  .house-panel--ashby .caption-box { color: var(--red); }
</style>
</head>
<body>

<!-- Marok House -->
<section class="house-panel house-panel--marok">
  <svg class="namesake-photo" viewBox="0 0 596 596" role="img" aria-label="Cut-out black and white portrait of Eli Marok seated, tinted yellow">
    <defs><linearGradient id="g-marok" x1="0" y1="0" x2="1" y2="1"><stop offset="0" stop-color="#6b6a4a"/><stop offset="1" stop-color="#cfcfb6"/></linearGradient></defs>
    <path d="M236 600 C236 520 290 480 360 470 L400 300 C410 220 440 140 490 132 C545 126 585 165 600 200 L600 600 Z" fill="url(#g-marok)" stroke="#fff" stroke-width="8"/>
  </svg>
  <div class="house-tab" style="left:14px;height:124px;">
    <svg viewBox="0 0 140 124" preserveAspectRatio="none" aria-hidden="true"><path d="M0 0H140V124L70 98 0 124Z" fill="#fff"/></svg>
    <div class="house-tab__label" style="padding-top:18px;"><span class="house-tab__name">MAROK</span><span class="house-tab__word">HOUSE</span></div>
  </div>
  <p class="college-name" style="top:24px;"><strong>Tarnbrook Secondary</strong><span>College</span></p>
  <h2 class="namesake-name" style="left:22px;top:252px;font-size:76px;">Eli Marok</h2>
  <p class="namesake-quote" style="left:34px;top:346px;width:330px;font-size:20px;line-height:1.3;">“I lay awake picturing the days ahead. The way I hoped they would be, even if I am gone.”</p>
  <p class="caption-box" style="top:500px;width:238px;height:72px;">known for his work championing community land stewardship and for a landmark case that reshaped how island families held their ancestral lands. 1931- 1990</p>
</section>

<!-- Strand House -->
<section class="house-panel house-panel--strand">
  <svg class="namesake-photo" viewBox="0 0 596 596" role="img" aria-label="Cut-out portrait of Joe Strand wearing a striped scarf, tinted blue">
    <defs><linearGradient id="g-strand" x1="0" y1="0" x2="1" y2="1"><stop offset="0" stop-color="#9fdcf6"/><stop offset="1" stop-color="#0a5f8a"/></linearGradient></defs>
    <path d="M326 600 L326 390 C380 370 420 350 430 300 C420 240 430 160 490 124 C550 100 600 130 600 150 L600 600 Z" fill="url(#g-strand)" stroke="#fff" stroke-width="8"/>
  </svg>
  <div class="house-tab" style="left:34px;">
    <svg viewBox="0 0 140 136" preserveAspectRatio="none" aria-hidden="true"><path d="M0 0H140V136L70 110 0 136Z" fill="#fff"/></svg>
    <div class="house-tab__label" style="padding-top:28px;"><span class="house-tab__name" style="font-size:29px;">STRAND</span><span class="house-tab__word">HOUSE</span></div>
  </div>
  <p class="college-name" style="top:36px;"><strong>Tarnbrook Secondary</strong><span>College</span></p>
  <h2 class="namesake-name" style="left:36px;top:200px;font-size:64px;">Joe Strand</h2>
  <p class="namesake-quote" style="left:36px;top:292px;width:300px;font-size:18px;line-height:1.26;">“I love every day. There’s always a hill to climb, new friends to make… You’ve just got to find what lights you up and chase it. That’s where the fire is, that’s how you find where you belong.”</p>
  <p class="caption-box" style="top:502px;width:316px;height:88px;">Joe Strand: one of the league’s best-loved figures, who won its top player award in 1988. Off the field, he was a respected club leader, fundraiser, youth mentor and author. 1962-2010</p>
</section>

<!-- Vale House -->
<section class="house-panel house-panel--vale">
  <svg class="namesake-photo" viewBox="0 0 596 596" role="img" aria-label="Cut-out portrait of aviator Nora Vale in flying cap and goggles, tinted teal">
    <defs><linearGradient id="g-vale" x1="0" y1="0" x2="1" y2="1"><stop offset="0" stop-color="#bfeee4"/><stop offset="1" stop-color="#0f4d44"/></linearGradient></defs>
    <path d="M350 600 L350 470 C380 440 370 380 360 330 C350 260 370 200 420 175 C480 145 560 150 600 190 L600 600 Z" fill="url(#g-vale)" stroke="#fff" stroke-width="8"/>
  </svg>
  <div class="house-tab" style="left:32px;">
    <svg viewBox="0 0 140 136" preserveAspectRatio="none" aria-hidden="true"><path d="M0 0H140V136L70 110 0 136Z" fill="#fff"/></svg>
    <div class="house-tab__label" style="padding-top:32px;"><span class="house-tab__name">VALE</span><span class="house-tab__word">HOUSE</span></div>
  </div>
  <p class="college-name" style="top:36px;"><strong>Tarnbrook Secondary</strong><span>College</span></p>
  <h2 class="namesake-name" style="left:32px;top:226px;font-size:62px;">Nora Vale</h2>
  <p class="namesake-quote" style="left:35px;top:300px;width:310px;font-size:18.5px;line-height:1.22;">“As a young girl I used to dream I could soar. I could dream I could float high above the gum trees while the storms rolled in across the plains below me at night”</p>
  <p class="caption-box" style="top:484px;width:400px;height:100px;padding-top:16px;">Nora Vale: a pioneering aviator who flew medical supplies to remote stations, and the founder of a flying club that trained young women as pilots. 1918-2004</p>
</section>

<!-- Ashby House -->
<section class="house-panel house-panel--ashby">
  <svg class="namesake-photo" viewBox="0 0 596 596" role="img" aria-label="Cut-out portrait of Hattie Ashby in a dark dress with medals, tinted red">
    <defs><linearGradient id="g-ashby" x1="0" y1="0" x2="1" y2="1"><stop offset="0" stop-color="#d8b3a6"/><stop offset="1" stop-color="#2a0e0e"/></linearGradient></defs>
    <path d="M318 600 C360 520 420 480 450 460 C430 400 440 340 460 300 C450 250 490 170 540 150 C570 140 600 150 600 160 L600 600 Z" fill="url(#g-ashby)" stroke="#fff" stroke-width="8"/>
  </svg>
  <div class="house-tab" style="left:34px;">
    <svg viewBox="0 0 140 136" preserveAspectRatio="none" aria-hidden="true"><path d="M0 0H140V136L70 110 0 136Z" fill="#fff"/></svg>
    <div class="house-tab__label" style="padding-top:28px;"><span class="house-tab__name">ASHBY</span><span class="house-tab__word">HOUSE</span></div>
  </div>
  <p class="college-name" style="top:36px;"><strong>Tarnbrook Secondary</strong><span>College</span></p>
  <h2 class="namesake-name" style="left:44px;top:230px;font-size:68px;">Hattie Ashby</h2>
  <p class="namesake-quote" style="left:40px;top:312px;width:360px;font-size:22px;line-height:1.22;">“Weak eyes narrow your view. Weak vision narrows your life.”</p>
  <p class="caption-box" style="top:484px;width:318px;height:100px;padding-top:18px;">Hattie Ashby: a blind writer and teacher who founded a society to print and share books for readers of braille 1869-1941</p>
</section>

</body>
</html>
```